Business Cards

Business cards (double-sided) to be handed out to clients and potential clients, with contact details, logo .

Target Market(s)

Small to medium size businesses

Industry/Entity Type

Accountants

Contact Information for Business Card

Brightwater Ledger & Counsel Ltd

Colors

Designer to choose only greyscale colors for use in the design.

Requirements
Must have
• Name, Title, Address, Phone number, Email, Website
Nice to have
• Modern, clean lines, classy
Should not have
• Business cards to be double-sided. Form keeps reverting to single-sided.

```html
<!DOCTYPE html>
<html lang="en">
<head>
<meta charset="utf-8">
<title>Brightwater Ledger &amp; Counsel — Business Cards</title>
<link href="https://fonts.googleapis.com/css2?family=Montserrat:wght@400;500;700&display=swap" rel="stylesheet">
<style>
  :root {
    --backdrop: #3b3735;
    --paper: #ffffff;
    --band-grey: #7d7d7d;
    --card-dark: #2a2a2a;
    --back-black: #1e1e1e;
    --back-mark: #2e2e2e;
    --ink: #1c1c1c;
    --ink-light: #ffffff;
    --ink-muted: #d8d8d8;
  }
  * { margin: 0; padding: 0; box-sizing: border-box; }
  html, body { width: 1200px; height: 786px; overflow: hidden; }
  body {
    background: var(--backdrop);
    font-family: "Montserrat", sans-serif;
    position: relative;
  }
  .card {
    position: absolute;
    top: 243px;
    width: 510px;
    height: 300px;
    overflow: hidden;
    box-shadow: 0 10px 30px rgba(0,0,0,.35);
  }
  .card-front { left: 60px; background: var(--paper); }
  .card-back { left: 630px; background: var(--back-black); }

  .front-brand {
    position: absolute;
    top: 0; left: 0; right: 0;
    height: 160px;
    display: flex;
    align-items: center;
    justify-content: center;
    gap: 12px;
  }
  .brand-square {
    width: 14px; height: 14px;
    background: var(--ink);
  }
  .brand-name {
    font-weight: 500;
    font-size: 22px;
    letter-spacing: 1.5px;
    color: var(--ink);
    text-transform: uppercase;
  }
  .name-band {
    position: absolute;
    top: 160px; left: 0; right: 0;
    height: 48px;
    background: var(--band-grey);
    text-align: center;
    padding-top: 6px;
    color: var(--ink-light);
  }
  .person-name { font-weight: 700; font-size: 19px; line-height: 22px; }
  .person-title { font-size: 11px; color: var(--ink-muted); }

  .contact-band {
    position: absolute;
    top: 208px; left: 0; right: 0; bottom: 0;
    background: var(--card-dark);
    color: var(--ink-light);
    display: flex;
    align-items: center;
  }
  .address {
    width: 250px;
    text-align: right;
    padding-right: 22px;
    font-size: 13px;
    line-height: 18px;
  }
  .divider {
    width: 1px; height: 52px;
    background: var(--ink-muted);
  }
  .contact-list {
    list-style: none;
    padding-left: 20px;
    font-size: 12px;
    line-height: 17px;
  }
  .contact-list li { display: flex; align-items: center; gap: 8px; }
  .contact-list svg { width: 10px; height: 10px; fill: var(--ink-light); flex: none; }

  .back-brand {
    position: absolute;
    inset: 0;
    display: flex;
    align-items: center;
    justify-content: center;
    gap: 12px;
  }
  .back-brand .brand-square { background: var(--back-mark); }
  .back-brand .brand-name { color: var(--back-mark); }
</style>
</head>
<body>
  <section class="card card-front" aria-label="Business card front">
    <div class="front-brand">
      <span class="brand-square"></span>
      <span class="brand-name">Brightwater Ledger &amp; Counsel</span>
    </div>
    <div class="name-band">
      <div class="person-name">Anders Holt</div>
      <div class="person-title">Owner</div>
    </div>
    <div class="contact-band">
      <div class="address">Here is your full address<br>Road number #18 Eastport</div>
      <div class="divider"></div>
      <ul class="contact-list">
        <li><svg viewBox="0 0 10 10"><path d="M2 0.5 L4 2.5 L3 3.8 Q4.5 6 6.2 7 L7.5 6 L9.5 8 L8 9.5 Q4 9 0.5 2 Z"/></svg>+49 404 555 0182</li>
        <li><svg viewBox="0 0 10 10"><path d="M0 2 H10 V8 H0 Z M0.8 2.6 L5 5.6 L9.2 2.6" stroke="#2a2a2a" stroke-width=".8"/></svg>info@brightwaterledger.com</li>
        <li><svg viewBox="0 0 10 10"><circle cx="5" cy="5" r="4.5"/><path d="M0.5 5 H9.5 M5 0.5 V9.5" stroke="#2a2a2a" stroke-width=".7"/></svg>www.brightwaterledger.com</li>
      </ul>
    </div>
  </section>

  <section class="card card-back" aria-label="Business card back">
    <div class="back-brand">
      <span class="brand-square"></span>
      <span class="brand-name">Brightwater Ledger &amp; Counsel</span>
    </div>
  </section>
</body>
</html>
```